UI Design & Web Design for Used Car Dealer.
Modern and user friendly responsive layout for mobiles and desktop. Bootstrap and form elements for members,registration process,login,dashboard. Layouts for Home Page, Car Listing Pages, Individual Car Information page and etc.

Output files in Bootstrap Html/CSS
Please refer to attachments for more details.

Target Market(s)

Asia / Singapore

Industry/Entity Type

Car Dealer

Coding

Coded - Design and coding required

Number of Pages Required

5+ page

Font styles to use
Sans Serif

Colors
acd037
f6faec
cfcfcf
b1b1b1
ffffff

Requirements
Must have
• Coded in Bootstrap 3 UI Elements, Forms, Labels, Sections, Tables, Buttons, Alerts, Modal, Fonts, Dashboard, Login, Register,Contact
Nice to have
• Stock Images
Should not have
• NA

```html
<!DOCTYPE html>
<html lang="en">
<head>
<meta charset="utf-8">
<title>Drivora – Sign Up</title>
<link href="https://fonts.googleapis.com/css2?family=Open+Sans:wght@400;600&family=Roboto:wght@300;400;500;700&display=swap" rel="stylesheet">
<style>
  :root{
    --green:#acd037;
    --button:#b3d34f;
    --page:#f8f8f8;
    --white:#ffffff;
    --field:#f2f2f2;
    --rule:#dcdcdc;
    --text:#444444;
    --muted:#9a9a9a;
    --icon:#8a8a8a;
  }
  *{box-sizing:border-box;margin:0;padding:0}
  html,body{width:1200px;height:742px;overflow:hidden}
  body{background:var(--page);font-family:"Roboto",sans-serif;color:var(--text);position:relative}

  .site-header{position:absolute;left:0;top:0;width:1200px;height:58px;background:var(--white);border-bottom:1px solid #e4e4e4}
  .brand{position:absolute;left:89px;top:17px;font-family:"Open Sans",sans-serif;font-weight:600;font-size:20px;letter-spacing:2px;color:var(--green);text-transform:uppercase}
  .main-nav{position:absolute;right:90px;top:0;height:58px;display:flex;font-family:"Open Sans",sans-serif;font-size:13px;text-transform:uppercase}
  .main-nav a{display:block;height:58px;line-height:62px;padding:0 14px;color:#333;text-decoration:none;position:relative}
  .main-nav a.is-active{color:var(--green)}
  .main-nav a.is-active::before{content:"";position:absolute;left:-4px;right:-4px;top:0;height:3px;background:var(--green)}

  .signup-card{position:absolute;left:197px;top:118px;width:806px;height:486px;background:var(--white)}
  .signup-title{position:absolute;left:0;width:100%;top:70px;text-align:center;font-weight:300;font-size:23px;color:#333}
  .signup-title::after{content:"";display:block;width:31px;height:2px;background:var(--green);margin:12px auto 0}

  .signup-form{position:absolute;left:63px;top:135px;width:684px;display:grid;grid-template-columns:338px 338px;column-gap:6px;row-gap:6px}
  .field{height:43px;background:var(--field);border-radius:2px;display:flex;align-items:center;padding-left:17px;font-size:13px;color:#555;position:relative}
  .field svg{width:13px;height:13px;fill:var(--icon);margin-right:9px;flex:none}
  .field .caret{position:absolute;right:18px;top:19px;width:0;height:0;border-left:5px solid transparent;border-right:5px solid transparent;border-top:6px solid #999}
  .submit-btn{height:44px;background:var(--button);border:0;border-radius:2px;color:var(--white);font-family:"Roboto",sans-serif;font-weight:700;font-size:15px;letter-spacing:.3px;text-transform:uppercase;margin-left:2px}

  .login-link{position:absolute;left:0;width:100%;top:350px;text-align:center;font-size:14.5px;color:#555}
  .login-note{position:absolute;left:0;width:100%;top:378px;text-align:center;font-size:14px;color:var(--muted)}

  .site-footer{position:absolute;left:0;top:690px;width:1200px;height:52px;background:var(--white)}
  .site-footer::before{content:"";position:absolute;left:89px;right:89px;top:0;height:1px;background:var(--rule)}
  .copyright{position:absolute;left:0;width:100%;top:19px;text-align:center;font-family:"Open Sans",sans-serif;font-size:12.5px;color:#333}
</style>
</head>
<body>
  <header class="site-header">
    <div class="brand">Drivora</div>
    <nav class="main-nav">
      <a class="is-active" href="#">Home</a>
      <a href="#">Benefits</a>
      <a href="#">Vehicle Listings</a>
      <a href="#">Start Advertising Now</a>
      <a href="#">Contact</a>
    </nav>
  </header>

  <main class="signup-card">
    <h1 class="signup-title">SIgn Up in to Drivora</h1>
    <form class="signup-form">
      <div class="field">
        <svg viewBox="0 0 16 16"><path d="M1 8l7-7h6v6l-7 7z M11 3.5a1.5 1.5 0 1 0 .01 0z"/></svg>Title<span class="caret"></span>
      </div>
      <div class="field">
        <svg viewBox="0 0 16 16"><circle cx="8" cy="4.5" r="3.5"/><path d="M1.5 16c0-4 3-6.5 6.5-6.5s6.5 2.5 6.5 6.5z"/></svg>First Name
      </div>
      <div class="field">
        <svg viewBox="0 0 16 16"><circle cx="8" cy="4.5" r="3.5"/><path d="M1.5 16c0-4 3-6.5 6.5-6.5s6.5 2.5 6.5 6.5z"/></svg>Last Name
      </div>
      <div class="field">
        <svg viewBox="0 0 16 16"><path d="M1 3h14v10H1z M1.5 3.5L8 9l6.5-5.5" stroke="#f2f2f2" stroke-width="1.2"/></svg>Email Address
      </div>
      <div class="field">
        <svg viewBox="0 0 16 16"><path d="M3.5 1l3 3-1.8 2c1 2 2.3 3.3 4.3 4.3l2-1.8 3 3-2 2.5C6.5 14 2 9.5 1 3.5z"/></svg>Mobile Phone No
      </div>
      <div class="field">
        <svg viewBox="0 0 16 16"><path d="M4 7V5a4 4 0 0 1 8 0v2h1.5v9h-11V7zm2 0h4V5a2 2 0 0 0-4 0z"/></svg>Password
      </div>
      <div class="field">
        <svg viewBox="0 0 16 16"><path d="M4 7V5a4 4 0 0 1 8 0v2h1.5v9h-11V7zm2 0h4V5a2 2 0 0 0-4 0z"/></svg>Confirm Password
      </div>
      <button class="submit-btn" type="button">Submit</button>
    </form>
    <p class="login-link">Already registered ? Login Here</p>
    <p class="login-note">The Email address will be used as username for login.</p>
  </main>

  <footer class="site-footer">
    <p class="copyright">Copyright Drivora 2016 | All Right Reserved</p>
  </footer>
</body>
</html>
```